Trifold Brochure

This is relatively easy. We already have a trifold made we simply want to update the LOOK to look more like our current website. All content would stay the same the only thing that would change would be the fonts, colors and background images to match the current website.

I have attached a word doc of the old trifold brochure. We would want the content to remain on the same pages of the trifold. Again all you are doing is updating the font, logo, colors and any background images. Please comment with any questions.

This is a 5 day project!

Requirements
Must have
• Logo, colors and fonts to match our current website.
http://www.brambleworksgroup.example/

```html
<!DOCTYPE html>
<html lang="en">
<head>
<meta charset="utf-8">
<title>Trifold Brochure – Inside Spread</title>
<link href="https://fonts.googleapis.com/css2?family=Arimo:wght@400;700&display=swap" rel="stylesheet">
<style>
:root{
  --backdrop:#a3a3a3;
  --paper:#e4efd2;
  --band-dark:#7c9660;
  --band-mid:#b9d09b;
  --band-soft:#d3e4bb;
  --ink:#2f3a26;
  --accent:#85a263;
  --check:#5f7a45;
  --on-dark:#f1f6e8;
  --fold:rgba(90,110,70,.18);
}
*{box-sizing:border-box;margin:0;padding:0}
html,body{width:1200px;height:800px;overflow:hidden}
body{background:var(--backdrop);font-family:"Arimo",Arial,sans-serif;color:var(--ink)}
.brochure{position:absolute;left:50px;top:50px;width:1100px;height:700px;background:var(--paper);overflow:hidden;box-shadow:0 6px 18px rgba(0,0,0,.25)}
.top-strip{position:absolute;left:0;top:0;width:100%;height:10px;background:var(--band-dark)}
.fold{position:absolute;top:0;bottom:0;width:1px;background:var(--fold)}
.fold--1{left:366px}.fold--2{left:733px}
.piling-drawing{position:absolute;left:90px;top:24px;width:560px;height:250px;background:radial-gradient(ellipse at 20% 40%,rgba(130,160,100,.14),rgba(130,160,100,0) 60%)}

.section-title{color:var(--accent);font-weight:700;font-size:15px;margin-bottom:7px}
.includes{position:absolute;left:34px;top:28px;width:670px}
.checklist{list-style:none;font-size:11px;line-height:1.4}
.checklist li{position:relative;padding-left:20px;margin-bottom:4px}
.checklist svg{position:absolute;left:0;top:2px}
.flexibility{position:absolute;left:34px;top:218px;width:670px;font-size:11px;line-height:1.4}

.standards{position:absolute;left:748px;top:26px;width:334px;font-size:8px;line-height:1.3}
.standards .section-title{font-size:11px;margin-bottom:5px}
.standards ol{padding-left:14px}
.standards ol ol{list-style:lower-alpha;padding-left:14px}
.standards li{margin-bottom:2px}

.mid-band{position:absolute;left:0;top:330px;width:100%;height:130px}
.intro{position:absolute;left:34px;top:348px;width:1040px;font-size:11px;line-height:1.36}

.lower{position:absolute;left:0;top:445px;width:100%;height:255px;background:var(--band-dark)}

.column{position:absolute;top:414px}
.col--raise{left:20px;width:336px}
.col--repair{left:390px;width:326px}
.col--new{left:757px;width:320px}
.photo-row{display:flex;align-items:flex-end;gap:6px;height:62px}
.photo{width:130px;height:62px}
.photo--raise{background:linear-gradient(160deg,#7ea3c6,#8a8f6a 60%,#c9b14a)}
.photo--repair{background:linear-gradient(180deg,#8a9aa8,#6b4f33 50%,#9a7a55)}
.photo--new{background:linear-gradient(150deg,#f3f1ec,#d9d4ca 60%,#c7a48a)}
.tile{width:24px;height:24px;background:var(--band-soft)}
.tile--icon{background:var(--accent);display:flex;align-items:center;justify-content:center}
.col-heading{color:var(--on-dark);font-weight:700;font-size:13px;line-height:15px;text-transform:uppercase;margin:8px 0 4px}
.col-body{color:var(--on-dark);font-size:9px;line-height:1.32;text-align:justify}

.contact-bar{position:absolute;left:366px;top:636px;width:734px;height:64px;background:var(--band-soft);display:flex;align-items:center;gap:14px;padding:0 24px;font-size:11px;line-height:1.5}
.contact-bar .brand-dot{width:30px;height:30px;border-radius:50%;background:var(--accent);flex:none}
.contact-bar .brand-name{font-weight:700}
</style>
</head>
<body>
<main class="brochure">
  <div class="top-strip"></div>
  <div class="piling-drawing" role="img" aria-label="Faint line drawing of a piling collar system in the background"></div>

  <section class="includes">
    <h2 class="section-title">Our System includes:</h2>
    <ul class="checklist">
      <li><svg width="12" height="12" viewBox="0 0 12 12"><path d="M1 6l3 3 7-7" stroke="#5f7a45" stroke-width="2" fill="none"/></svg>Collar cut to customer length in sizes ranging from 12" to 144".</li>
      <li><svg width="12" height="12" viewBox="0 0 12 12"><path d="M1 6l3 3 7-7" stroke="#5f7a45" stroke-width="2" fill="none"/></svg>Collar Cap with galvanized steel u-bolts to connect to the structure.</li>
      <li><svg width="12" height="12" viewBox="0 0 12 12"><path d="M1 6l3 3 7-7" stroke="#5f7a45" stroke-width="2" fill="none"/></svg>Collar spacers to allow for variations in Piling diameter.</li>
      <li><svg width="12" height="12" viewBox="0 0 12 12"><path d="M1 6l3 3 7-7" stroke="#5f7a45" stroke-width="2" fill="none"/></svg>Collar Cap spacers to allow for variations in Piling diameter.</li>
      <li><svg width="12" height="12" viewBox="0 0 12 12"><path d="M1 6l3 3 7-7" stroke="#5f7a45" stroke-width="2" fill="none"/></svg>Tubes of high strength adhesive glue to connect the Piling to the Collar and for the Collar flange and to fill gaps between the Piling and the Collar due to the nature of irregular Pilings.</li>
      <li><svg width="12" height="12" viewBox="0 0 12 12"><path d="M1 6l3 3 7-7" stroke="#5f7a45" stroke-width="2" fill="none"/></svg>Detailed installation manual providing guidance to the installation contractor.</li>
      <li><svg width="12" height="12" viewBox="0 0 12 12"><path d="M1 6l3 3 7-7" stroke="#5f7a45" stroke-width="2" fill="none"/></svg>Detailed written specifications provided in paper format and available in word format upon request.</li>
    </ul>
  </section>

  <section class="flexibility">
    <h2 class="section-title">Flexibility:</h2>
    <p>Our system has been designed to accommodate piles ranging in diameter from 8" to 12". The system can also correct vertical alignments by up to 6 degrees.</p>
  </section>

  <section class="standards">
    <h2 class="section-title">General Performance Standards, Notes and Guidance:</h2>
    <ol>
      <li>General Performance Standards:
        <ol>
          <li>Vertical loading (vertical compression) 90 Kips</li>
          <li>Bending moment 65 ft-Kips</li>
          <li>Shear (lateral forces) 10 Kips</li>
          <li>Alignment/plumbness correction 6 Deg.</li>
        </ol>
      </li>
      <li>This document and information provided is the property of BWG and shall not be altered, used or referenced by any third party without the expressed written permission of BWG.</li>
      <li>The User of this system is advised that they should obtain services of a design professional for the use of this product. BWG only represents that our product will withstand loading as documented in our specifications. The design professional shall evaluate the loading conditions and determine if the loading conditions fall within the parameters of the Collar system. Additionally, the user should employ the design professional to inspect the Pilings to ensure they are acceptable for use.</li>
      <li>Local Permitting may be required for use of this product. Consult with your local code official prior to use.</li>
      <li>The User of this system should employ installation contractors that have adequate skills for the required work. BWG does not and cannot attest to any skill set or quality of work of any installer.</li>
      <li>The written instructions for installation must be followed. Failure to do so could result in failure of the system.</li>
    </ol>
  </section>

  <svg class="mid-band" viewBox="0 0 1100 130" preserveAspectRatio="none" aria-hidden="true">
    <path d="M0 14 Q550 -6 1100 4 L1100 130 L0 130 Z" fill="#b9d09b"/>
  </svg>
  <p class="intro">Our Patented Piling system has been designed to withstand the corrosive environment of beach communities. The salt water and windblown sand corrodes unprotected materials, and yes, even stainless steel. Our system utilizes a high strength carbon fiber material that is corrosion proof from salt water and UV proof. The system will not erode, decay or loose strength over time. The system has three installation conditions, for raising a house on existing pilings, repairing damaged pilings, and for connecting new pilings to floor joists in new construction. The three options are generally described below:</p>

  <div class="lower"></div>

  <section class="column col--raise">
    <div class="photo-row">
      <div class="photo photo--raise" role="img" aria-label="Photo of an excavator beside a house raised on pilings"></div>
      <div class="tile tile--icon"><svg width="16" height="16" viewBox="0 0 16 16"><path d="M2 7L8 2l6 5M4 7v7h8V7" stroke="#f1f6e8" stroke-width="1.5" fill="none"/></svg></div>
      <div class="tile"></div><div class="tile"></div>
    </div>
    <h3 class="col-heading">Raising a Structure</h3>
    <p class="col-body">A house on pilings can be raised by disconnecting the house from the pilings, raise the house to create a work area, cut all of the piles to a preset elevation, and install the Collar on the piling. The Collar is connected to the piling by six galvanized lag bolts and is glued with a high strength adhesive and all gaps are filled with flowable epoxy fill and fiber. The Collar extends above the piling to the bottom of the home's joists to the preset height, up to 6'-6", or higher when lateral supports are considered. Once the Collar is set on the home, it is filled with concrete to transfer the load of the house from the floor joists directly to the top of the piling, the concrete provides the compressive strength, while the Collar provides tensile and shear strength. A Collar Cap is then installed with two galvanized steel u-bolts which extend into the floor joists for the installer to connect to the joists.</p>
  </section>

  <section class="column col--repair">
    <div class="photo-row">
      <div class="photo photo--repair" role="img" aria-label="Photo of a shingled beach house standing on extended pilings"></div>
      <div class="tile tile--icon"><svg width="16" height="16" viewBox="0 0 16 16"><path d="M3 2v12M6.5 2v12M10 2v12M13 2v12" stroke="#f1f6e8" stroke-width="1.5"/></svg></div>
      <div class="tile"></div><div class="tile"></div>
    </div>
    <h3 class="col-heading">Piling Repairs and Extensions</h3>
    <p class="col-body">A 36" section of Collar can be installed onto an existing piling and a new section of piling can be placed on top, with 18" of the Collar covering the top of the existing and 18" covering the bottom of the new piling. Generally, the minimum length of the new piling needs to be 6 feet to ensure the piling length is not too short, which could lead to reduced piling loading capacity. This option generally requires lateral support of the pilings. Consult with your design professional.</p>
  </section>

  <section class="column col--new">
    <div class="photo-row">
      <div class="photo photo--new" role="img" aria-label="Photo of hands reviewing construction plans on a table"></div>
      <div class="tile tile--icon"><svg width="16" height="16" viewBox="0 0 16 16"><path d="M2 14L2 4l12 10z" stroke="#f1f6e8" stroke-width="1.5" fill="none"/></svg></div>
      <div class="tile"></div><div class="tile"></div>
    </div>
    <h3 class="col-heading">New Construction</h3>
    <p class="col-body">The standard practice for connecting pilings to floor joists is to notch the pilings and bolt the joists to the pilings. This method dramatically reduces the strength of the piling due to reduced cross sectional area at the connection point. Additionally, this connection method exposes more surface area of the piling allowing for additional potential for dry rot. A 12" Collar section with a Collar Cap can be used to connect directly to the top of the new piling providing a connection that will outlast the piling by literally thousands of years.</p>
  </section>

  <footer class="contact-bar">
    <span class="brand-dot" aria-hidden="true"></span>
    <div>
      <span class="brand-name">Brambleworks Group, LLC</span> - PO Box 4410 - Fernbrook Hollow, PA 19990-0400 &nbsp;|&nbsp; www.brambleworksgroup.example<br>
      T. 555.014.2270 &nbsp;|&nbsp; F. 555.014.2281 &nbsp;|&nbsp; Email: sales@brambleworksgroup.example
    </div>
  </footer>

  <div class="fold fold--1"></div>
  <div class="fold fold--2"></div>
</main>
</body>
</html>
```